Halloween Style Website Design

We need a website design with a Halloween theme.

I have provided 3 wireframes to work from. If you like you can just design the homepage first. If we like your designs we will instruct you to design the other pages once we narrow them down.

The website will be totally halloween themed. We will use vector type designs.

We want a feel similar to this style I guess:

https://v.plomrix.com/mv/KatrE72wq0Lb/toplarge.jpg
https://cdn.quellory.com/people/5813207/captures/4127396/panel_4__1_.jpg
https://cdn3.glyvanto.com/p/1000x1000/51/38/halloween-castle-background-design-vector-40617385.jpg
https://pix.drumvale.com/free-vector/decorative-halloween-background-flat-style_41-3075186249.jpg?size=626&ext=jpg
https://bx4.qernil.net/jpg/05/19/43/86/500_F_519438621_hTzWmKcLoPsRaYx3NbvGdEqUiFjO8wMe.jpg

```html
<!DOCTYPE html>
<html lang="en">
<head>
<meta charset="utf-8">
<title>Hollow Lantern — Sell Soul</title>
<link href="https://fonts.googleapis.com/css2?family=Creepster&family=Freckle+Face&family=Questrial&display=swap" rel="stylesheet">
<style>
  :root{
    --night:#1b1b33;
    --night-deep:#18182c;
    --hill:#1f1f3d;
    --dim-brown:#4a3a31;
    --dim-link:#3c3c60;
    --dim-text:#3f3f66;
    --modal:#121212;
    --field:#3a3a3a;
    --field-text:#e6e6e6;
    --pumpkin:#f6b536;
    --ink:#111111;
  }
  *{box-sizing:border-box;margin:0;padding:0}
  html,body{width:1200px;height:675px;overflow:hidden;background:var(--night-deep)}
  body{position:relative;font-family:"Questrial",sans-serif}

  .hero-scene{position:absolute;left:0;top:0;width:1200px;height:450px;
    background:
      radial-gradient(ellipse 190px 170px at 258px 200px,rgba(70,70,110,.55),transparent 80%),
      radial-gradient(ellipse 420px 260px at 200px 300px,rgba(40,40,75,.7),transparent 85%),
      radial-gradient(ellipse 260px 240px at 1120px 230px,rgba(34,34,66,.8),transparent 85%),
      linear-gradient(180deg,#1e1e3b 0%,#222246 60%,#1f1f3e 100%)}
  .hero-scene::after{content:"";position:absolute;left:0;top:0;width:410px;height:450px;
    background:linear-gradient(150deg,rgba(210,210,225,.14) 0%,rgba(210,210,225,0) 55%)}
  .ground{position:absolute;left:0;top:400px;width:1200px;height:80px}

  .site-nav{position:absolute;left:0;top:0;width:1200px;height:72px}
  .brand{position:absolute;left:27px;top:19px;font-family:"Freckle Face",cursive;font-size:28px;line-height:32px;color:var(--dim-brown)}
  .nav-links{list-style:none}
  .nav-links li{position:absolute;top:23px;font-size:19px;line-height:24px;color:var(--dim-link);white-space:nowrap}
  .nav-login{position:absolute;left:977px;top:23px;font-family:"Freckle Face",cursive;font-size:19px;line-height:24px;color:var(--dim-brown)}
  .nav-signup{position:absolute;left:1056px;top:20px;width:101px;height:31px;background:var(--dim-brown);
    clip-path:polygon(0 0,100% 3%,99% 97%,1% 100%);font-family:"Freckle Face",cursive;font-size:18px;color:var(--night-deep);
    display:flex;align-items:center;justify-content:center}

  .hero-copy{position:absolute;left:600px;top:178px;width:420px}
  .hero-copy h1{font-family:"Creepster",cursive;font-weight:400;font-size:34px;line-height:40px;color:var(--dim-brown);text-align:right;white-space:nowrap}
  .hero-copy p{margin-top:19px;font-size:16px;line-height:18.5px;color:var(--dim-text)}
  .learn-more{position:absolute;left:753px;top:317px;width:153px;height:47px;background:var(--dim-brown);
    clip-path:polygon(0 0,100% 6%,99% 100%,1% 96%);font-family:"Creepster",cursive;font-size:22px;color:var(--night-deep);
    display:flex;align-items:center;justify-content:center}

  .features{position:absolute;left:187px;top:540px;width:826px;height:135px;display:flex;gap:19px}
  .feature{flex:1;text-align:center;background:var(--night)}
  .feature h2{font-family:"Creepster",cursive;font-weight:400;font-size:40px;line-height:48px;color:var(--dim-brown);margin-top:23px}
  .feature-art{width:120px;height:50px;margin:14px auto 0;background:linear-gradient(180deg,#3a302c,#252338);border-radius:10px 10px 0 0}

  .backdrop{position:absolute;inset:0;background:rgba(6,6,16,.12)}

  .signup-modal{position:absolute;left:450px;top:145px;width:300px;height:386px;background:var(--modal);border-radius:8px}
  .modal-close{position:absolute;right:15px;top:15px;width:11px;height:11px}
  .modal-title{margin-top:20px;text-align:center;font-family:"Freckle Face",cursive;font-weight:400;font-size:31px;line-height:38px;color:var(--pumpkin)}
  .signup-form{position:absolute;left:19px;top:76px;width:262px;height:300px}
  .field{display:block;width:262px;height:31px;margin-bottom:13px;background:var(--field);border:0;border-radius:2px;
    padding:0 9px;font-family:"Questrial",sans-serif;font-size:16px;color:var(--field-text)}
  .field::placeholder{color:var(--field-text)}
  .terms{display:flex;align-items:center;gap:6px;font-size:14px;color:#e0e0e0;white-space:nowrap}
  .terms-box{width:22px;height:22px;background:var(--field);border-radius:2px;flex:none}
  .submit{position:absolute;left:80px;top:257px;width:101px;height:31px;background:var(--pumpkin);border:0;
    clip-path:polygon(0 4%,100% 0,98% 94%,2% 100%);font-family:"Freckle Face",cursive;font-size:18px;color:var(--ink)}
</style>
</head>
<body>
  <div class="hero-scene" role="img" aria-label="Halloween night scene: cobweb with hanging spider, full moon, haunted house, werewolf on a hill, bats and a bare tree"></div>
  <svg class="ground" viewBox="0 0 1200 80" aria-hidden="true">
    <path d="M0 32 Q300 10 640 36 T1200 26 V80 H0Z" fill="var(--night-deep)"/>
  </svg>

  <header class="site-nav">
    <div class="brand">Hollow Lantern</div>
    <ul class="nav-links">
      <li style="left:591px">Home</li>
      <li style="left:686px">Build</li>
      <li style="left:772px">Tricks</li>
      <li style="left:863px">Treats</li>
    </ul>
    <div class="nav-login">Log In</div>
    <div class="nav-signup">Sign Up</div>
  </header>

  <section class="hero-copy">
    <h1>Welcome to Hollow Lantern</h1>
    <p>Lorem ipsum dolor sit amet, consectetuer adipiscing elit, sed diam nonummy nibh euismod tincidunt ut laoreet dolore magna aliquam erat volutpat.</p>
  </section>
  <div class="learn-more">Learn More</div>

  <section class="features">
    <article class="feature"><h2>Build</h2><div class="feature-art" role="img" aria-label="Gravestone illustration"></div></article>
    <article class="feature"><h2>Tricks</h2><div class="feature-art" role="img" aria-label="Cauldron illustration"></div></article>
    <article class="feature"><h2>Treats</h2><div class="feature-art" role="img" aria-label="Candy and ghost illustration"></div></article>
  </section>

  <div class="backdrop"></div>

  <div class="signup-modal" role="dialog" aria-label="Sell Soul">
    <svg class="modal-close" viewBox="0 0 11 11" aria-label="Close"><path d="M1 1L10 10M10 1L1 10" stroke="#e6e6e6" stroke-width="1.4" stroke-linecap="round"/></svg>
    <h2 class="modal-title">Sell Soul</h2>
    <form class="signup-form">
      <input class="field" type="text" placeholder="First Name">
      <input class="field" type="text" placeholder="Last Name">
      <input class="field" type="email" placeholder="Email">
      <input class="field" type="password" placeholder="Desired Password">
      <input class="field" type="password" placeholder="Repeat Password">
      <label class="terms"><span class="terms-box"></span>I agree to the terms and conditions</label>
      <button class="submit" type="button">Sign Up</button>
    </form>
  </div>
</body>
</html>
```